Business Card Design

We need a new business card design for our company, Lumen Forge.

Our website: www.brightrow7.ca

We are open to all ideas, from professional to very creative.
Updates

Design update requests:

1. We would like to see some examples with "BrightRow7" instead of "Lumen Forge" as the company name.
2. Would like to see "Software | Web | Branding" included on the card somewhere as well.

Thanks.

We are really trying to express the nature of our business through our business card.  "Lumen" can be misconstrued for the health industry, so use of "BrightRow7" and the "Software | Web | Branding" slogan are key to understanding our business.

We have uploaded a new PSD which includes a monitor, tablet, and phone screen.  This represents the flexibility of web applications and is another tool we would like to see used on business cards.

We will be eliminating designs today and will await updated designs with these new specs.

Thank-you.

Industry/Entity Type

Business

Requirements
Must have
• Content:
First M. Last
Managing Partner
e. email@brightrow7.ca
p. 555.555.5555

```html
<!DOCTYPE html>
<html lang="en">
<head>
<meta charset="utf-8">
<title>BrightRow7 Business Card</title>
<link rel="stylesheet" href="https://fonts.googleapis.com/css2?family=Open+Sans:wght@300;400;600&display=swap">
<style>
  :root {
    --page-bg: #e9eaec;
    --card-bg: #ffffff;
    --ink-dark: #4a4d52;
    --ink-mid: #5d6066;
    --ink-soft: #8a8d92;
    --blue-light: #8fd0f2;
    --blue-mid: #3aa6dd;
    --blue-deep: #2a6f96;
    --bar-edge: #d6d8db;
  }
  * { margin: 0; padding: 0; box-sizing: border-box; }
  html, body {
    width: 1200px;
    height: 900px;
    overflow: hidden;
    background: var(--page-bg);
    font-family: "Open Sans", Arial, sans-serif;
  }
  .canvas {
    position: relative;
    width: 1200px;
    height: 900px;
  }
  .card {
    position: absolute;
    left: 280px;
    width: 640px;
    height: 366px;
    background: var(--card-bg);
    box-shadow: 0 6px 22px rgba(0, 0, 0, 0.14);
    overflow: hidden;
  }
  .card--contact { top: 66px; }
  .card--brand { top: 468px; }

  /* Contact side */
  .pattern-area {
    position: absolute;
    left: 0;
    top: 24px;
    width: 230px;
    height: 318px;
    background: linear-gradient(135deg, var(--blue-deep) 0%, var(--blue-mid) 50%, var(--blue-light) 100%);
    clip-path: polygon(0 8%, 55% 0, 100% 22%, 100% 70%, 78% 100%, 0 100%);
  }
  .person {
    position: absolute;
    right: 46px;
    top: 58px;
    text-align: right;
  }
  .person__name {
    font-weight: 300;
    font-size: 44px;
    letter-spacing: 1px;
    color: var(--ink-mid);
    line-height: 1.1;
  }
  .person__role {
    font-size: 12px;
    color: var(--ink-soft);
    margin-top: 2px;
  }
  .contact {
    position: absolute;
    left: 262px;
    top: 196px;
    font-weight: 300;
    font-size: 24px;
    color: var(--ink-mid);
    line-height: 1.45;
  }

  /* Brand side */
  .brand {
    position: absolute;
    left: 0;
    right: 0;
    top: 96px;
    display: flex;
    justify-content: center;
    align-items: center;
    gap: 16px;
  }
  .brand__mark {
    width: 40px;
    height: 40px;
    background: var(--blue-mid);
  }
  .brand__name {
    font-weight: 600;
    font-size: 40px;
    color: var(--ink-dark);
    letter-spacing: 0.5px;
  }
  .divider-bar {
    position: absolute;
    left: 128px;
    top: 194px;
    width: 384px;
    height: 22px;
    background: var(--card-bg);
    border: 1px solid var(--bar-edge);
    box-shadow: 0 4px 6px rgba(0, 0, 0, 0.16);
  }
  .tagline {
    position: absolute;
    left: 0;
    right: 0;
    top: 228px;
    text-align: center;
    font-size: 19px;
    letter-spacing: 0.6px;
    color: var(--ink-dark);
  }
</style>
</head>
<body>
<main class="canvas">
  <section class="card card--contact">
    <div class="pattern-area" role="img" aria-label="Decorative block pattern of blue squares"></div>
    <div class="person">
      <p class="person__name">First M. Last</p>
      <p class="person__role">Managing Partner</p>
    </div>
    <div class="contact">
      <p>e. email@brightrow7.ca</p>
      <p>p. 555.555.5555</p>
    </div>
  </section>

  <section class="card card--brand">
    <div class="brand">
      <span class="brand__mark"></span>
      <span class="brand__name">BrightRow7</span>
    </div>
    <div class="divider-bar"></div>
    <p class="tagline">Software | Web | Branding</p>
  </section>
</main>
</body>
</html>
```